Need a Modern, Professional Website Design for Life Coaching Company in United States

Need Life Coaching Website Design for Life Coaching Company in the United States to wow and attract clients. Need a modern professional website to land clients.
- I am looking for an inspirational-looking website. Most of my clients will be female, but I want to attract both male and female clients, but I want to more females, site should be more feminine that masculine but attract both.

Target Market(s)

Adult women and men age 30 - 58

Colors
0054AA
0677BA
7BADD7
CADEEF
E8F1F8

Requirements
Must have
• modern, professional feel

```html
<!DOCTYPE html>
<html lang="en">
<head>
<meta charset="utf-8">
<title>Onward Path Coaching</title>
<link href="https://fonts.googleapis.com/css2?family=Dancing+Script:wght@500&family=Poppins:wght@400;500;600;700&family=Satisfy&display=block" rel="stylesheet">
<style>
:root{
  --navy:#0054AA;
  --blue:#0677BA;
  --sky:#7BADD7;
  --pale:#CADEEF;
  --mist:#E8F1F8;
  --ink:#1b1b1b;
  --text:#333;
  --white:#fff;
}
*{box-sizing:border-box;margin:0;padding:0}
html,body{width:1200px;height:5102px;overflow:hidden}
body{font-family:'Poppins',sans-serif;color:var(--text);background:var(--white);position:relative}
.script{font-family:'Satisfy','Dancing Script','Brush Script MT',cursive}
.section{position:absolute;left:0;width:1200px}
.btn{display:inline-block;font-weight:600;font-size:14px;text-decoration:none}

/* brand (text only) */
.brand{position:absolute;display:flex;flex-direction:column;align-items:center;font-weight:700;color:var(--navy);line-height:1}
.brand-line{font-size:30px;letter-spacing:1px}
.brand-sub{font-size:20px;letter-spacing:1px;margin-top:4px}

/* header */
.site-header{top:0;height:120px}
.site-header .brand{left:75px;top:30px}
.main-nav{position:absolute;right:75px;top:54px;display:flex;gap:46px;font-size:14px;font-weight:600;color:#222}
.main-nav .active{color:var(--blue)}

/* hero */
.hero{top:120px;height:662px}
.hero-photo{position:absolute;inset:0;background:linear-gradient(90deg,#f2d49a 0%,#e8b878 30%,#c9a272 55%,#8c9aa6 80%,#6f8497 100%)}
.hero-photo::after{content:"";position:absolute;left:0;right:0;bottom:0;height:45%;background:linear-gradient(180deg,rgba(150,165,180,0) 0%,rgba(110,130,150,.55) 100%)}
.hero-copy{position:absolute;left:75px;top:156px;width:560px}
.hero-copy h1{font-size:39px;line-height:50px;font-weight:700;color:var(--ink)}
.hero-copy p{margin-top:14px;width:520px;font-size:23px;line-height:35px;font-weight:600;color:var(--blue)}
.hero-copy p strong{color:var(--ink)}
.hero-actions{margin-top:20px;display:flex;gap:12px}
.hero-actions .btn{background:var(--blue);color:var(--white);padding:20px 28px;font-size:13px}

/* headings */
.title{text-align:center;font-size:44px;line-height:58px;font-weight:600;color:var(--ink)}
.title .accent{color:var(--blue);font-weight:700}
.rule{width:142px;height:5px;background:var(--blue);margin:22px auto 0}

/* services */
.services{top:860px;height:500px}
.card-row{position:absolute;left:75px;display:flex;gap:28px}
.card{width:242px;background:var(--mist);text-align:center}
.services .card-row{top:197px}
.services .card{height:226px;padding-top:36px}
.services .card h3{margin-top:14px;font-size:23px;line-height:31px;font-weight:600;color:var(--ink)}
.arrow{position:absolute;top:298px;width:22px;height:22px}
.icon{width:72px;height:72px;display:block;margin:0 auto}

/* about */
.about{top:1364px;height:553px;background:var(--navy);overflow:hidden}
.about-copy{position:absolute;left:75px;top:82px;width:520px;color:var(--white)}
.about-copy h2{font-size:42px;font-weight:600}
.about-copy .rule{margin:22px 0 0;width:142px;background:var(--white)}
.about-copy p{margin-top:28px;font-size:15px;line-height:32px}
.btn-outline{margin-top:32px;border:2px solid var(--white);color:var(--white);padding:12px 42px}
.about-photo{position:absolute;left:617px;top:66px;width:620px;height:424px;border-radius:230px 0 0 230px;background:linear-gradient(120deg,#cfcac2 0%,#9aa3ad 45%,#5e6a78 100%)}

/* how */
.how{top:1970px;height:830px}
.how .card-row{top:154px}
.how .card{height:298px;padding-top:36px}
.how .card h3{margin-top:16px;font-size:23px;line-height:31px;font-weight:600;color:var(--blue)}
.how .card p{margin-top:16px;font-size:14px;line-height:26px;padding:0 14px}
.how-text{position:absolute;top:502px;left:75px;display:flex;gap:60px;font-size:14px;line-height:29px}
.how-text p{width:460px}
.how-text p+p{width:505px}
.btn-blue-outline{position:absolute;left:510px;top:722px;width:180px;text-align:center;border:2px solid var(--blue);color:var(--blue);padding:14px 0}

/* benefits */
.benefits{top:2832px;height:518px;background:linear-gradient(160deg,#2f6fb5 0%,#2b78c4 45%,#3c86d0 100%)}
.benefits h2{margin-top:62px;text-align:center;font-size:44px;font-weight:600;color:var(--white)}
.benefit-cols{position:absolute;top:198px;left:75px;display:flex;gap:70px}
.benefit-cols ul{list-style:none;width:470px}
.benefit-cols li{position:relative;padding-left:32px;margin-bottom:22px;font-size:16px;line-height:26px;color:var(--white)}
.benefit-cols li svg{position:absolute;left:0;top:5px}

/* welcome */
.welcome{top:3420px;height:560px}
.welcome-copy{position:absolute;left:75px;top:62px;width:510px}
.welcome-copy h2{font-size:44px;font-weight:600;color:var(--ink)}
.welcome-copy h2 .accent{color:var(--blue);font-weight:700}
.welcome-copy .rule{margin:16px 0 0}
.welcome-copy p{margin-top:34px;font-size:14px;line-height:29px}
.welcome-copy p+p{margin-top:10px}
.signoff{margin-top:10px;font-size:30px;color:var(--blue)}
.portrait{position:absolute;left:643px;top:14px;width:486px;height:486px;border-radius:50%;background:radial-gradient(circle at 50% 40%,#e9e2dc 0%,#c9c2bc 60%,#a9a39e 100%)}

/* get started */
.start{top:4104px;height:700px;background:linear-gradient(180deg,#2d5f9c 0%,#1f5596 45%,#2e6eb6 100%)}
.quote{position:absolute;left:165px;top:-74px;width:870px;height:154px;background:var(--pale);text-align:center;padding-top:26px;color:var(--ink);z-index:2}
.quote .line{font-size:40px;line-height:50px}
.quote cite{display:block;font-style:normal;font-size:32px;line-height:40px;color:var(--blue)}
.start h2{position:absolute;top:150px;width:100%;text-align:center;font-size:44px;font-weight:600;color:var(--white)}
.start .lead{position:absolute;top:262px;left:100px;width:1000px;text-align:center;font-size:16px;line-height:32px;color:var(--white)}
.field{position:absolute;border:2px solid rgba(255,255,255,.85);color:var(--white);font-size:14px;padding:16px 16px}
.submit{position:absolute;left:435px;top:566px;width:332px;height:52px;background:var(--pale);color:var(--ink);text-align:center;line-height:52px;font-weight:600;font-size:17px}

/* footer */
.site-footer{top:4804px;height:298px;font-size:16px;color:#222}
.site-footer .brand{left:75px;top:112px}
.site-footer .brand-line{font-size:28px}
.site-footer .brand-sub{font-size:19px}
.copyright{position:absolute;left:75px;top:188px;font-size:13px;line-height:26px}
.footer-col{position:absolute;top:72px}
.footer-col h4{font-size:20px;font-weight:600;color:var(--blue);margin-bottom:6px}
.footer-col li{list-style:none;line-height:38px;display:flex;align-items:center;gap:16px}
.social{display:flex;gap:18px;margin-top:12px}
.social span{width:24px;height:24px;background:#444;border-radius:3px}
</style>
</head>
<body>

<header class="section site-header">
  <div class="brand"><span class="brand-line">ONWARD PATH</span><span class="brand-sub">COACHING</span></div>
  <nav class="main-nav">
    <span class="active">HOME</span><span>COACHING</span><span>COURSES</span><span>ABOUT US</span><span>CONTACT US</span>
  </nav>
</header>

<section class="section hero">
  <div class="hero-photo" role="img" aria-label="Woman in an orange sweater with arms spread wide, smiling toward a golden sunset over the sea"></div>
  <div class="hero-copy">
    <h1>YOU FEEL STUCK OR STAGNANT IN REACHING YOUR GOALS?</h1>
    <p>Gain clarity, confidence, accountability, and support to <strong>MOVE FORWARD &amp; ACHIEVE SUCCESS.</strong></p>
    <div class="hero-actions"><span class="btn">START COURSE</span><span class="btn">LEARN MORE</span></div>
  </div>
</section>

<section class="section services">
  <h2 class="title"><span class="accent">Coaching Services</span> to Help You<br>Pivot and Prosper</h2>
  <div class="rule"></div>
  <svg class="arrow" style="left:36px" viewBox="0 0 22 22"><circle cx="11" cy="11" r="10" fill="var(--blue)"/><path d="M13 6l-5 5 5 5M8 11h8" stroke="#fff" stroke-width="2" fill="none"/></svg>
  <svg class="arrow" style="left:1142px" viewBox="0 0 22 22"><circle cx="11" cy="11" r="10" fill="var(--blue)"/><path d="M9 6l5 5-5 5M14 11H6" stroke="#fff" stroke-width="2" fill="none"/></svg>
  <div class="card-row">
    <div class="card">
      <svg class="icon" viewBox="0 0 72 72" fill="none" stroke="var(--blue)" stroke-width="2"><rect x="30" y="8" width="32" height="24"/><path d="M36 16h20M36 22h14"/><circle cx="18" cy="18" r="6"/><path d="M10 44v-12h16l8-6"/><circle cx="22" cy="52" r="4"/><circle cx="36" cy="52" r="4"/><circle cx="50" cy="52" r="4"/><path d="M14 66v-4a8 8 0 0116 0M28 66v-4a8 8 0 0116 0M42 66v-4a8 8 0 0116 0"/></svg>
      <h3>Career<br>Coaching</h3>
    </div>
    <div class="card">
      <svg class="icon" viewBox="0 0 72 72" fill="none" stroke="var(--blue)" stroke-width="2"><circle cx="24" cy="18" r="9"/><circle cx="48" cy="18" r="9"/><path d="M8 66V44a14 14 0 0128 0v22M36 66V44a14 14 0 0128 0v22M24 36v8M48 36v8"/></svg>
      <h3>Relationship<br>Coaching</h3>
    </div>
    <div class="card">
      <svg class="icon" viewBox="0 0 72 72" fill="none" stroke="var(--blue)" stroke-width="2"><circle cx="36" cy="34" r="10"/><path d="M20 64v-6a16 16 0 0132 0v6"/><rect x="6" y="10" width="14" height="10"/><circle cx="60" cy="14" r="6"/><path d="M20 15l8 8M54 18l-8 6M36 6v14"/><rect x="52" y="40" width="12" height="12"/></svg>
      <h3>Mindset<br>Coaching</h3>
    </div>
    <div class="card">
      <svg class="icon" viewBox="0 0 72 72" fill="none" stroke="var(--blue)" stroke-width="3"><path d="M60 30A26 26 0 1148 14"/><path d="M46 6l4 9-9 3"/><path d="M36 20v16h12"/></svg>
      <h3>Life Reset<br>Coaching</h3>
    </div>
  </div>
</section>

<section class="section about">
  <div class="about-copy">
    <h2>About Us</h2>
    <div class="rule"></div>
    <p>Onward Path Coaching offers coaching services for adult women and men willing and ready to work hard to create the life they crave. Whether you want to increase your confidence, discover your life's purpose, land your dream job, or improve your relationships, we would be happy to help you reach your goals.</p>
    <span class="btn btn-outline">Read More</span>
  </div>
  <div class="about-photo" role="img" aria-label="Man with a headset working on a laptop and taking notes at a desk"></div>
</section>

<section class="section how">
  <h2 class="title"><span class="accent">How Coaching</span> Works</h2>
  <div class="rule"></div>
  <div class="card-row">
    <div class="card">
      <svg class="icon" viewBox="0 0 72 72" fill="none" stroke="var(--blue)" stroke-width="2"><circle cx="40" cy="30" r="18"/><circle cx="40" cy="30" r="13"/><path d="M27 43L10 60l4 4 17-17"/><path d="M40 22a6 6 0 00-3 11v4h6v-4a6 6 0 00-3-11z"/></svg>
      <h3>Discovery<br>Call</h3>
      <p>Neque porro quisquam est qui dolorem ipsum quia dolor sit amet.</p>
    </div>
    <div class="card">
      <svg class="icon" viewBox="0 0 72 72" fill="none" stroke="var(--blue)" stroke-width="2"><rect x="8" y="6" width="56" height="16" rx="3"/><rect x="8" y="28" width="56" height="16" rx="3"/><rect x="8" y="50" width="56" height="16" rx="3"/><circle cx="17" cy="14" r="3"/><path d="M26 14h20M16 36h20M16 58h14"/></svg>
      <h3 style="margin-top:26px">Sign Up</h3>
      <p style="margin-top:22px">Neque porro quisquam est qui dolorem ipsum quia dolor sit amet.</p>
    </div>
    <div class="card">
      <svg class="icon" viewBox="0 0 72 72" fill="none" stroke="var(--blue)" stroke-width="2"><path d="M14 4h32l10 10v54H14z"/><path d="M46 4v10h10"/><path d="M22 24h4M30 24h18M22 34h4M30 34h18M22 44h4M30 44h18M22 54h4M30 54h10"/><path d="M50 44l10 10-6 8-8-14z"/></svg>
      <h3>Pre-Coaching<br>Questionnaire</h3>
      <p>Neque porro quisquam est qui dolorem ipsum quia dolor sit amet.</p>
    </div>
    <div class="card">
      <svg class="icon" viewBox="0 0 72 72" fill="none" stroke="var(--blue)" stroke-width="2"><rect x="26" y="6" width="20" height="24"/><path d="M30 14h12M30 20h12"/><circle cx="14" cy="26" r="5"/><circle cx="58" cy="26" r="5"/><path d="M4 60V40h14v20M54 60V40h14v20M18 46h36M36 46v18M8 60v6M64 60v6"/></svg>
      <h3>1:1 Coaching<br>Session</h3>
      <p>Neque porro quisquam est qui dolorem ipsum quia dolor sit amet.</p>
    </div>
  </div>
  <div class="how-text">
    <p>You can choose a 30 or 60-minute phone or video session. Onward Path Coaching offers a 90-Day Jump Start Coaching Program to help you set goals and take action. Individual coaching sessions range in price from $50.00 to $75.00. Deep down, you know you desire success. So, get started today! Get the life you crave!</p>
    <p>Like an athletic coach, a life coach comes alongside you to encourage, equip, and empower you to succeed. Your life coach will work with you to discover your passion, set realistic goals, create plans, and take action. Through goal-setting strategies, transformational coaching, and accountability, you will have a firm foundation to help you live a purposeful, abundant life.</p>
  </div>
  <span class="btn btn-blue-outline">Read More</span>
</section>

<section class="section benefits" role="img" aria-label="Blue-tinted winding mountain road through a forest">
  <h2>Benefits of Life Coaching Include</h2>
  <div class="benefit-cols">
    <ul>
      <li><svg width="16" height="16" viewBox="0 0 16 16"><circle cx="8" cy="8" r="8" fill="#fff"/><path d="M4 8l3 3 5-6" stroke="var(--blue)" stroke-width="2" fill="none"/></svg>Accountability and support to help you succeed</li>
      <li><svg width="16" height="16" viewBox="0 0 16 16"><circle cx="8" cy="8" r="8" fill="#fff"/><path d="M4 8l3 3 5-6" stroke="var(--blue)" stroke-width="2" fill="none"/></svg>Overcome obstacles</li>
      <li><svg width="16" height="16" viewBox="0 0 16 16"><circle cx="8" cy="8" r="8" fill="#fff"/><path d="M4 8l3 3 5-6" stroke="var(--blue)" stroke-width="2" fill="none"/></svg>Gain clarity about what you want</li>
      <li><svg width="16" height="16" viewBox="0 0 16 16"><circle cx="8" cy="8" r="8" fill="#fff"/><path d="M4 8l3 3 5-6" stroke="var(--blue)" stroke-width="2" fill="none"/></svg>Thrive from your God-given purpose</li>
      <li><svg width="16" height="16" viewBox="0 0 16 16"><circle cx="8" cy="8" r="8" fill="#fff"/><path d="M4 8l3 3 5-6" stroke="var(--blue)" stroke-width="2" fill="none"/></svg>Happiness from pursuing and reaching goals</li>
    </ul>
    <ul>
      <li><svg width="16" height="16" viewBox="0 0 16 16"><circle cx="8" cy="8" r="8" fill="#fff"/><path d="M4 8l3 3 5-6" stroke="var(--blue)" stroke-width="2" fill="none"/></svg>Encouragement and guidance to help you stay on track</li>
      <li><svg width="16" height="16" viewBox="0 0 16 16"><circle cx="8" cy="8" r="8" fill="#fff"/><path d="M4 8l3 3 5-6" stroke="var(--blue)" stroke-width="2" fill="none"/></svg>Strategies to help you reach goals faster</li>
      <li><svg width="16" height="16" viewBox="0 0 16 16"><circle cx="8" cy="8" r="8" fill="#fff"/><path d="M4 8l3 3 5-6" stroke="var(--blue)" stroke-width="2" fill="none"/></svg>Energy from doing what excites</li>
      <li><svg width="16" height="16" viewBox="0 0 16 16"><circle cx="8" cy="8" r="8" fill="#fff"/><path d="M4 8l3 3 5-6" stroke="var(--blue)" stroke-width="2" fill="none"/></svg>Joy from doing what you love</li>
      <li><svg width="16" height="16" viewBox="0 0 16 16"><circle cx="8" cy="8" r="8" fill="#fff"/><path d="M4 8l3 3 5-6" stroke="var(--blue)" stroke-width="2" fill="none"/></svg>Increase productivity</li>
    </ul>
  </div>
</section>

<section class="section welcome">
  <div class="welcome-copy">
    <h2><span class="accent">Welcome</span> Message</h2>
    <div class="rule"></div>
    <p>Hi. I am Renee Calloway. I'm a life and career coach. I'm so excited that you are here, ready to take control of your destiny. Like you, I've experienced my share of life's ups, downs, twists, and turns. To overcome those challenges, I remained committed, resilient, and optimistic about my goals and lifelong learning. Most importantly, I couldn't give up because too much was at stake. I had to Move Forward. So, I am asking you, are you ready to Move Forward to live beyond your wildest dreams? If so, I invite you to contact me today to learn more.</p>
    <p>Let's partner together and co-create your desired future.</p>
    <div class="signoff script">Cheers! Renee</div>
  </div>
  <div class="portrait" role="img" aria-label="Portrait of the coach, a smiling woman with glasses"></div>
</section>

<section class="section start" role="img" aria-label="Blue-tinted winding road through a wooded valley at dusk">
  <blockquote class="quote script"><div class="line">When you are going through hell, keep going!</div><cite>Marcus Ellery</cite></blockquote>
  <h2>Get Started Today</h2>
  <p class="lead">Request a free 15-minute phone consultation to see how we can help you achieve your goals. Step boldly into your greatness. Contact us today to start living a happier, more fulfilled, meaningful life.</p>
  <div class="field" style="left:255px;top:382px;width:337px;height:56px">Name</div>
  <div class="field" style="left:608px;top:382px;width:337px;height:56px">Email Address</div>
  <div class="field" style="left:255px;top:444px;width:690px;height:112px">Comments</div>
  <div class="submit">Submit Now</div>
</section>

<footer class="section site-footer">
  <div class="brand"><span class="brand-line">ONWARD PATH</span><span class="brand-sub">COACHING</span></div>
  <p class="copyright">Copyright © 2023 Company Name<br>All Right Reserved</p>
  <div class="footer-col" style="left:377px">
    <h4>Site Map</h4>
    <ul><li>Home</li><li>Coaching Services</li><li>FAQ</li><li>About Us</li><li>Contact Us</li></ul>
  </div>
  <div class="footer-col" style="left:588px">
    <h4>Contact Us</h4>
    <ul>
      <li><svg width="16" height="16" viewBox="0 0 16 16"><path d="M8 1a5 5 0 015 5c0 4-5 9-5 9S3 10 3 6a5 5 0 015-5z" fill="var(--blue)"/><circle cx="8" cy="6" r="2" fill="#fff"/></svg>Brookfield, OH</li>
      <li><svg width="16" height="16" viewBox="0 0 16 16"><path d="M4 1l3 3-2 2a8 8 0 005 5l2-2 3 3-2 3C7 15 1 9 1 3z" fill="var(--blue)"/></svg>555-014-2290</li>
      <li><svg width="16" height="16" viewBox="0 0 16 16"><rect x="1" y="3" width="14" height="10" fill="var(--blue)"/><path d="M1 3l7 6 7-6" stroke="#fff" fill="none"/></svg>hello@onwardpath.example</li>
    </ul>
  </div>
  <div class="footer-col" style="left:906px">
    <h4>Follow Us</h4>
    <div class="social"><span></span><span></span><span></span><span></span></div>
  </div>
</footer>

</body>
</html>
```